wooden jewelry - pearl necklaces

I sell wooden jeweler (rings and pearls) on markets, and so on. I also opened my business as a carpenter. The rings and a combination of wood and metal. The wood is special wood, not very common on Europe. I paint the rings afterwards. You can see some of the pictures on the pictures I uploaded. The pearls are made of the same kind of wood and colored in all kinds of colors. They are then assembled to bracelets. The jewelry is very individual and looks really cool and all kinds of people.

Target Market(s)

Young urban alternative with a sense of individuality

Contact Information for Business Card

Front:

Text:

„Kugelwerk“ (big)
„Malte Oswitz“ (smaler)

Back
„Holzschmuck
Herstellung von individuellem Holz- und Modeschmuck

Malte Oswitz
Tel: 015239460518
Lindgarbweg 9
83127 Burghausen

malteoswitz@postfeld.de“

Font styles to use
Sans Serif

Requirements
Nice to have
• Nice to see a camel thorn tree on the background, this is a special wood and some of the rings are made out of this wood.

```html
<!DOCTYPE html>
<html lang="de">
<head>
<meta charset="utf-8">
<title>Kugelwerk – Visitenkarte</title>
<link rel="stylesheet" href="https://fonts.googleapis.com/css2?family=Bebas+Neue&family=Montserrat:wght@300;400&family=Playfair+Display:wght@700&display=swap">
<style>
  :root {
    --page-bg: #dcdedd;
    --card-bg: #ffffff;
    --card-edge: #3a3a3a;
    --ink: #2a2a2a;
    --ink-soft: #3c3c3c;
    --icon: #6b6b6b;
    --bead-dark: #3a2330;
    --bead-mid: #8a5a3a;
    --bead-light: #d9b98a;
    --bead-pale: #eddcb8;
  }
  * { box-sizing: border-box; margin: 0; padding: 0; }
  html, body { width: 976px; height: 1200px; overflow: hidden; }
  body { background: var(--page-bg); position: relative; font-family: "Montserrat", sans-serif; color: var(--ink); }

  .card {
    position: absolute; left: 44px; width: 875px; height: 528px;
    background: var(--card-bg); border: 1.5px solid var(--card-edge); overflow: hidden;
  }
  .card--front { top: 53px; }
  .card--back { top: 605px; }

  .bead-fill {
    position: absolute;
    background:
      radial-gradient(circle at 20% 40%, var(--bead-pale) 0 6%, transparent 14%),
      radial-gradient(circle at 55% 60%, var(--bead-dark) 0 7%, transparent 15%),
      radial-gradient(circle at 80% 30%, var(--bead-light) 0 6%, transparent 14%),
      linear-gradient(120deg, var(--bead-mid), var(--bead-light) 40%, var(--bead-mid) 70%, var(--bead-dark));
  }
  .card--front .bead-fill { left: 0; right: 0; top: 389px; bottom: 0; }
  .card--back .bead-fill { inset: 0; }

  .holder { position: absolute; left: 68px; top: 86px; }
  .holder__name { font-size: 29px; font-weight: 400; color: var(--ink); line-height: 1.2; }
  .holder__role { font-size: 22px; font-weight: 300; color: var(--ink-soft); margin-top: 2px; letter-spacing: 0.5px; }

  .product-shot {
    position: absolute; left: 40px; top: 172px; width: 335px; height: 200px;
    background: radial-gradient(ellipse at 50% 55%, #b07a5a 0%, #d9b79c 35%, #f6efe9 70%, #ffffff 100%);
  }

  .contact { position: absolute; left: 390px; top: 86px; list-style: none; }
  .contact__item { display: flex; align-items: flex-start; font-size: 25px; font-weight: 300; color: var(--ink-soft); line-height: 30px; }
  .contact__item + .contact__item { margin-top: 13px; }
  .contact__item--phone { margin-top: 20px !important; }
  .contact__icon { width: 36px; height: 30px; margin-right: 30px; flex: none; }
  .contact__icon svg { width: 36px; height: 30px; stroke: var(--icon); fill: none; stroke-width: 1.3; }

  .brand-panel {
    position: absolute; left: 81px; top: 97px; width: 714px; height: 334px;
    background: var(--card-bg); text-align: center; font-family: "Bebas Neue", sans-serif; color: var(--ink);
  }
  .brand__lead { margin-top: 66px; font-size: 40px; line-height: 1; display: flex; justify-content: center; align-items: flex-end; gap: 6px; }
  .brand__amp { font-family: "Playfair Display", serif; font-size: 80px; line-height: 0.7; font-weight: 700; margin: 0 -2px; }
  .brand__name { font-size: 82px; line-height: 1; margin-top: 14px; letter-spacing: 2px; }
  .brand__owner { font-size: 50px; line-height: 1; margin-top: 6px; letter-spacing: 0.5px; }
</style>
</head>
<body>

<section class="card card--front">
  <div class="holder">
    <p class="holder__name">Malte Oswitz</p>
    <p class="holder__role">Holzschmuck</p>
  </div>
  <div class="product-shot" role="img" aria-label="Foto einer Holzperlenkette mit zwei Holzringen"></div>

  <ul class="contact">
    <li class="contact__item">
      <span class="contact__icon"><svg viewBox="0 0 36 30"><path d="M18 28 C12 20 9 15 9 10.5 A9 9 0 0 1 27 10.5 C27 15 24 20 18 28Z"/><circle cx="18" cy="10.5" r="3.3"/></svg></span>
      <span>Lindgarbweg 9,<br>83127 Burghausen</span>
    </li>
    <li class="contact__item">
      <span class="contact__icon"><svg viewBox="0 0 36 30"><rect x="3" y="5" width="30" height="20"/><path d="M3 5 L18 17 L33 5 M3 25 L14 14 M33 25 L22 14"/></svg></span>
      <span>malteoswitz@postfeld.de</span>
    </li>
    <li class="contact__item">
      <span class="contact__icon"><svg viewBox="0 0 36 30"><circle cx="18" cy="15" r="13"/><ellipse cx="18" cy="15" rx="6" ry="13"/><path d="M5 15 H31 M7 8.5 H29 M7 21.5 H29 M18 2 V28"/></svg></span>
      <span>www.kugelwerk-holz.de</span>
    </li>
    <li class="contact__item contact__item--phone">
      <span class="contact__icon"><svg viewBox="0 0 36 30"><path d="M3 11 C3 4 33 4 33 11 L33 13 L26 13 L26 9 L10 9 L10 13 L3 13 Z"/><path d="M9 14 L27 14 L31 27 L5 27 Z"/><circle cx="18" cy="20" r="3.5"/></svg></span>
      <span>Tel. 015239460518</span>
    </li>
  </ul>

  <div class="bead-fill" role="img" aria-label="Foto vieler bunter Holzperlen"></div>
</section>

<section class="card card--back">
  <div class="bead-fill" role="img" aria-label="Foto vieler bunter Holzperlen"></div>
  <div class="brand-panel">
    <p class="brand__lead"><span>Individueller Holz-</span><span class="brand__amp">&amp;</span><span>Modeschmuck</span></p>
    <p class="brand__name">Kugelwerk</p>
    <p class="brand__owner">Malte Oswitz</p>
  </div>
</section>

</body>
</html>
```